Singer Song writer needs a CD cover Design

I need a cover design to a 4 pages digipak. ( Front, inside, CD-tray and back) And a digital cover art. And a design for the CD

I want it clear and simple. The name of my album is "Skyggelandet" which means refleksions in danish. I play folk-rock, pop and country

I don't no about the pictures. Maybe you can use it somewhere in the design. And maybe not.
Updates

I like the designs I have received so far. Thank you very much for a god job.I was wondering if some of you would try to make a design without my pictures. Where you can create your own interpretation of the title "Skyggelandet". It could be very interesting to see your meaning of that word.Skyggelandet means reflections in danish.You can make reflections over your life. Think about how you are living. But you can also reflect a light. The way we are living and what we are doing in life - are making light reflections.Does it make sense?Best regardsBrian Added Friday, November 20, 2015

Industry/Entity Type

Digital

Requirements
Must have
• My name and the Album's name:
• Skyggelandet
• Mikkel Torndahl
• A list of the songs
• 1: Sølv under sneen
• 2: Min sti, min vej
• 3: Bliv her lidt
• 4: Sidste tog mod nord
• 5: Sommer i marken
• 6: Lad bølgerne synge nu
• 7: Fjerne kyst
• 8: Lang sommer
• 9: Et digt om havets brusen
• And a description of the album
• Kære lytter
• Skyggelandet består af to dele. Fem sange, der er skrevet over temaet ”refleksioner”. Og en re-mastered udgave af sangene fra lovsangs EP’en ”Under åben himmel”.
• Jeg håber, du vil sætte dig godt til rette. Nyde et glas eller en kop. Og naturligvis nyde musikken.
• God fornøjelse.
• Medvirkende:
• Mikkel Torndahl: Vokal, klaver, akustisk guitar på #1 #2 #4 #5, kor på #1 #2 #3 #4 #5,
• Svend Lyngholt: Bas på #6 #7 #8 #9, elguitar på #1 #2 #3 #4
• Aksel Thorup Vinding: Bas på #1 #2 #3 #4
• Morten Ahlmann Brejning: Trommer
• Niels Krogsbæk Lauritzen: Akustisk guitar på #7 #8 #9, elguitar på #6 #8 #9, Lab Steel på #7 #9, Mandolin på #9
• Anders Vestergård Hjort: Elguitar på #1 #2 #4, akustisk guitar på #3
• Lise-Lotte Rask Hedegård: kor på #6 #7 #8 #9, vokal på #6 og #9
• Indspillet i Ørnereden Studio af Ole Kastrup Damgaard og Anders Vestergård Hjort
• Mikset og produceret af Anders Vestergård Hjort
• Alle sange er skrevet og komponeret af Mikkel Torndahl
Nice to have
• Interpretations of the word reflections

```html
<!DOCTYPE html>
<html lang="da">
<head>
<meta charset="utf-8">
<title>Skyggelandet – CD label</title>
<link rel="stylesheet" href="https://fonts.googleapis.com/css2?family=Roboto:wght@300&family=Source+Sans+3:wght@700&display=swap">
<style>
  :root {
    --page-bg: #ffffff;
    --rim: #bdbdbd;
    --water-deep: #070b1e;
    --water-mid: #17224d;
    --water-blue: #26357a;
    --glow-warm: #f6d9a6;
    --glow-amber: #c98a3e;
    --label-text: #ffffff;
    --hole: #ffffff;
  }
  html, body {
    margin: 0;
    padding: 0;
    width: 1200px;
    height: 1000px;
    overflow: hidden;
    background: var(--page-bg);
  }
  .disc-canvas {
    display: block;
    width: 1200px;
    height: 1000px;
  }
  .disc-rim {
    fill: none;
    stroke: var(--rim);
    stroke-width: 2;
  }
  .center-hole { fill: var(--hole); }
  .album-title {
    font-family: "Roboto", "Helvetica Neue", Arial, sans-serif;
    font-weight: 300;
    font-size: 61px;
    letter-spacing: -1px;
    fill: var(--label-text);
  }
  .album-title-reflection {
    font-family: "Roboto", "Helvetica Neue", Arial, sans-serif;
    font-weight: 300;
    font-size: 61px;
    letter-spacing: -1px;
  }
  .artist-name {
    font-family: "Source Sans 3", "Myriad Pro", Arial, sans-serif;
    font-weight: 700;
    font-size: 36px;
    letter-spacing: -0.5px;
    fill: var(--label-text);
  }
  .format-badge {
    fill: #ffffff;
    stroke: #1a1a1a;
    stroke-width: 1.5;
  }
</style>
</head>
<body>
<svg class="disc-canvas" viewBox="0 0 1200 1000" xmlns="http://www.w3.org/2000/svg">
  <defs>
    <clipPath id="label-area">
      <circle cx="600" cy="485" r="372"/>
    </clipPath>
    <radialGradient id="water-light" cx="600" cy="540" r="420" gradientUnits="userSpaceOnUse">
      <stop offset="0" stop-color="var(--glow-warm)"/>
      <stop offset="0.28" stop-color="var(--glow-amber)"/>
      <stop offset="0.5" stop-color="var(--water-blue)"/>
      <stop offset="0.78" stop-color="var(--water-mid)"/>
      <stop offset="1" stop-color="var(--water-deep)"/>
    </radialGradient>
    <linearGradient id="title-fade" x1="0" y1="266" x2="0" y2="236" gradientUnits="userSpaceOnUse">
      <stop offset="0" stop-color="#ffffff" stop-opacity="0.55"/>
      <stop offset="1" stop-color="#ffffff" stop-opacity="0"/>
    </linearGradient>
  </defs>

  <circle class="disc-rim" cx="600" cy="485" r="397"/>

  <g class="disc-label" clip-path="url(#label-area)">
    <rect class="label-artwork" x="228" y="113" width="744" height="744" fill="url(#water-light)"
          role="img" aria-label="Photograph of dark rippling night water reflecting a swirling cluster of sparkling golden lights"/>
  </g>

  <text class="album-title" x="600" y="265" text-anchor="middle">Skyggelandet</text>
  <text class="album-title-reflection" x="600" y="265" text-anchor="middle"
        fill="url(#title-fade)" transform="translate(0 533) scale(1 -1)" aria-hidden="true">Skyggelandet</text>

  <rect class="format-badge" x="291" y="441" width="73" height="47" rx="1"/>

  <circle class="center-hole" cx="600" cy="485" r="57"/>

  <text class="artist-name" x="585" y="781" text-anchor="middle">Mikkel Torndahl</text>
</svg>
</body>
</html>
```